Allergy Social Media Advertising Graphics Needed

We already have the copy written for KT and Vistaloop ads and need a designer to ad a graphic element to the campaign.

Target Market(s)

Mostly soccer moms, suburban Washington, DC, highly educated, smart and research oriented.

Font styles to use
Sans Serif

Requirements
Must have
• An eye-catching concept that makes people stop scrolling and pay attention to the advertisement.
Nice to have
• Clean and simple design. Bold approach with an elegant feel.
Should not have
• Too busy or cartoon-like designs.

```html
<!DOCTYPE html>
<html lang="en">
<head>
<meta charset="utf-8">
<title>Peanut Allergy Oral Immunotherapy Ad</title>
<link rel="stylesheet" href="https://fonts.googleapis.com/css2?family=Jost:wght@400;500&display=swap">
<style>
  :root {
    --peanut-deep: #3e2613;
    --peanut-dark: #5c3a1c;
    --peanut-mid: #8c5e33;
    --peanut-light: #b7854f;
    --peanut-glow: #c99a66;
    --card-white: #ffffff;
    --ink: #111111;
    --accent-sand: #d9bfa3;
  }
  html, body {
    margin: 0;
    padding: 0;
    width: 1200px;
    height: 1200px;
    overflow: hidden;
  }
  .ad-canvas {
    position: relative;
    width: 1200px;
    height: 1200px;
    overflow: hidden;
  }
  .peanut-backdrop {
    position: absolute;
    inset: 0;
    background:
      radial-gradient(ellipse 260px 200px at 12% 10%, var(--peanut-glow) 0%, transparent 70%),
      radial-gradient(ellipse 240px 220px at 90% 18%, var(--peanut-light) 0%, transparent 70%),
      radial-gradient(ellipse 260px 240px at 6% 62%, var(--peanut-light) 0%, transparent 70%),
      radial-gradient(ellipse 280px 220px at 94% 70%, var(--peanut-glow) 0%, transparent 70%),
      radial-gradient(ellipse 300px 200px at 30% 96%, var(--peanut-light) 0%, transparent 70%),
      radial-gradient(ellipse 280px 200px at 78% 98%, var(--peanut-mid) 0%, transparent 70%),
      radial-gradient(circle at 50% 50%, var(--peanut-mid) 0%, var(--peanut-dark) 60%, var(--peanut-deep) 100%);
  }
  .message-card {
    position: absolute;
    left: 86px;
    top: 86px;
    width: 1028px;
    height: 1028px;
    box-sizing: border-box;
    padding-top: 104px;
    background: var(--card-white);
    display: flex;
    flex-direction: column;
    align-items: center;
    text-align: center;
    font-family: "Jost", "Helvetica Neue", Arial, sans-serif;
    color: var(--ink);
    box-shadow: 0 10px 40px rgba(30, 15, 5, 0.35);
  }
  .headline,
  .answer {
    margin: 0;
    font-weight: 400;
    font-size: 92px;
    line-height: 110px;
    letter-spacing: 0.5px;
  }
  .divider {
    width: 240px;
    height: 22px;
    background: var(--accent-sand);
    margin: 74px 0 49px;
    flex: none;
  }
</style>
</head>
<body>
  <main class="ad-canvas">
    <div class="peanut-backdrop" role="img" aria-label="Close-up photograph of a pile of whole peanuts in their shells"></div>
    <section class="message-card">
      <h1 class="headline">Is worrying<br>about your child’s<br>peanut allergy<br>driving you nuts?</h1>
      <div class="divider"></div>
      <p class="answer">Oral immunotherapy<br>could help.</p>
    </section>
  </main>
</body>
</html>
```